Wanderlark Gin - Bottle Label for a craft Gin about to be launched on the world from New Zealand

We are a start up craft distillery in New Zealand. We have developed a wonderful Gin using our own grain spirit and both traditional and New Zealand native botanicals (Manuka to be specific), chosen our bottle and the name "Wanderlark" and done a bit of amateur label design and now we are looking for someone to make it great.

Feel free to change up our amateur concept but give us something that will pop from the back bar and scream authenticity, craft and individuality.

The attached files give you the specifications of the bottle, our current concept for a Wanderlark label and an earlier concept drawing that gives an idea of where we are thinking the two labels should go on the front of the bottle.

Thanks, we look forward to your ideas!!

Target Market(s)

High end and craft Gin drinkers. Hipsters and cocktail barflys and their bar tenders and bar owners

Font styles to use
Serif
Sans Serif
Decorative
Script

Requirements
Must have
• Attractive individuality
Nice to have
• Coolness
Should not have
• Uncoolness

```html
<!DOCTYPE html>
<html lang="en">
<head>
<meta charset="utf-8">
<title>Wanderlark Gin – Bottle Labels</title>
<link href="https://fonts.googleapis.com/css2?family=Arvo:wght@700&family=Roboto+Slab:wght@500;700&family=Cormorant+Garamond:wght@500&display=swap" rel="stylesheet">
<style>
  :root {
    --backdrop: #f1f1f1;
    --label-light: #ebe8da;
    --label-dark: #d6d1bd;
    --ink: #262624;
    --ink-soft: #55534c;
    --sprig: #c3b798;
    --rule: #8d897c;
    --strip: #141414;
    --strip-text: #a0402e;
  }
  * { margin: 0; padding: 0; box-sizing: border-box; }
  html, body {
    width: 1200px;
    height: 2341px;
    overflow: hidden;
    background: var(--backdrop);
  }
  .canvas {
    position: relative;
    width: 1200px;
    height: 2341px;
  }

  /* Front label */
  .front-label {
    position: absolute;
    left: 188px;
    top: 650px;
    width: 825px;
    height: 765px;
    background: linear-gradient(135deg, var(--label-light) 0%, var(--label-dark) 100%);
    color: var(--ink);
    overflow: hidden;
  }
  .sprig-art {
    position: absolute;
    left: 45px;
    top: 50px;
    width: 560px;
    height: 560px;
    border-radius: 45% 55% 50% 40%;
    background: radial-gradient(ellipse at 55% 45%, rgba(195,183,152,0.55) 0%, rgba(195,183,152,0.25) 50%, rgba(195,183,152,0) 72%);
  }
  .gin-name {
    position: absolute;
    left: 12px;
    top: 62px;
    font-family: "Arvo", "Rockwell", serif;
    font-weight: 700;
    font-size: 88px;
    letter-spacing: 4px;
    line-height: 1;
    text-transform: uppercase;
    text-shadow: 5px 4px 0 rgba(120,112,90,0.35);
    white-space: nowrap;
  }
  .gin-name .initial { font-size: 118px; }
  .gin-style {
    position: absolute;
    left: 478px;
    top: 242px;
    font-family: "Roboto Slab", serif;
    font-weight: 700;
    font-size: 30px;
    line-height: 37px;
    letter-spacing: 2px;
    text-transform: uppercase;
  }
  .strength {
    position: absolute;
    left: 45px;
    top: 468px;
    width: 730px;
    height: 72px;
    border-top: 3px solid var(--rule);
    border-bottom: 3px solid var(--rule);
    display: flex;
    align-items: center;
    justify-content: space-between;
    padding: 0 28px;
    font-family: "Roboto Slab", serif;
    font-weight: 500;
    font-size: 36px;
    letter-spacing: 2px;
    text-transform: uppercase;
  }
  .strength .divider {
    flex: 1;
    height: 2px;
    margin: 0 26px;
    background: var(--rule);
  }
  .maker {
    position: absolute;
    left: 150px;
    top: 585px;
    display: flex;
    align-items: center;
    gap: 14px;
    font-family: "Roboto Slab", serif;
    font-weight: 500;
    font-size: 20px;
    letter-spacing: 2px;
    text-transform: uppercase;
    color: var(--ink-soft);
  }
  .maker .mark {
    width: 26px;
    height: 26px;
    border: 3px solid var(--ink-soft);
    border-radius: 50%;
  }
  .volume {
    position: absolute;
    left: 330px;
    top: 640px;
    font-family: "Roboto Slab", serif;
    font-weight: 700;
    font-size: 32px;
    letter-spacing: 1px;
    text-transform: uppercase;
  }

  /* Story strip */
  .story-strip {
    position: absolute;
    left: 245px;
    top: 1545px;
    width: 711px;
    height: 144px;
    background: var(--strip);
    display: flex;
    align-items: center;
    justify-content: center;
    padding: 0 34px;
    -webkit-mask:
      radial-gradient(circle 8px at 0 50%, transparent 98%, #000 100%) left / 51% 24px repeat-y,
      radial-gradient(circle 8px at 100% 50%, transparent 98%, #000 100%) right / 51% 24px repeat-y;
    mask:
      radial-gradient(circle 8px at 0 50%, transparent 98%, #000 100%) left / 51% 24px repeat-y,
      radial-gradient(circle 8px at 100% 50%, transparent 98%, #000 100%) right / 51% 24px repeat-y;
  }
  .story-text {
    font-family: "Cormorant Garamond", "Garamond", serif;
    font-weight: 500;
    font-variant: small-caps;
    font-size: 24px;
    line-height: 27px;
    text-align: center;
    color: var(--strip-text);
    letter-spacing: 0.5px;
  }
</style>
</head>
<body>
<main class="canvas">

  <section class="front-label">
    <div class="sprig-art" role="img" aria-label="Engraved manuka sprig with blossoms and leaves"></div>
    <h1 class="gin-name"><span class="initial">W</span>anderlark</h1>
    <p class="gin-style">New Zealand<br>Small Batch<br>Gin</p>
    <div class="strength">
      <span>84 Proof</span>
      <span class="divider"></span>
      <span>42% Alc.</span>
    </div>
    <div class="maker">
      <span class="mark"></span>
      <span>Harbourline Distillery</span>
    </div>
    <p class="volume">500ml</p>
  </section>

  <section class="story-strip">
    <p class="story-text">
      A classically inspired Gin with a New Zealand twist. Distilled in-house starting
      with local grain and finished with 11 botanicals including a generous helping
      of East Coast Manuka cones, Gisborne Citrus and Otago Lavender
    </p>
  </section>

</main>
</body>
</html>
```